Brindlefax Brochure

I require a brochure for my business called Brindlefax Services or "Brindlefax" for short. We obtain subpoena material on behalf of lawfirms in Sydney and focus purely on the sydney-city based locations.

www.brindlefax-demo.com.au

My website is quite comprehensive and has all the information you may require.

The design should stand out as to price and trust to know we would complete the job professionally remember that my clients are law firms. I have a few documents that i will attach that will show you what i am looking for. I will leave colour upto the designer.

I require ongoing work including logos, other brochures so this will be an ongoing contract. I require someone who will communicate with me and is available for a range of projects.

Target Market(s)

Law firms

Industry/Entity Type

Business

Colors

Designer to choose colors to be used in the design.

Requirements
Must have
• professional and instill trust and security
Nice to have
• this market is dominated by 3 other firms we are a new firm looking to establish and take a number of their clients who are paying through the nose.

```html
<!DOCTYPE html>
<html lang="en">
<head>
<meta charset="utf-8">
<title>Brindlefax Services – Brochure</title>
<link rel="stylesheet" href="https://fonts.googleapis.com/css2?family=Oswald:wght@300;400;500&family=Source+Sans+3:wght@400;600&display=swap">
<style>
  :root {
    --page: #ffffff;
    --panel-mid: #ececed;
    --navy-dark: #1b2631;
    --slate: #4a5661;
    --slate-dark: #3f4b57;
    --bar-light: #e6e7e8;
    --pill-grey: #a7a9ac;
    --pill-light: #d8d9db;
    --heading-blue: #1f7dba;
    --ink: #1c1c1c;
    --contact-navy: #1d3557;
    --accent-red: #e2231a;
    --icon-blue: #5cbcec;
    --white: #ffffff;
  }
  * { box-sizing: border-box; margin: 0; padding: 0; }
  html, body { width: 1200px; height: 1000px; overflow: hidden; background: var(--page); }
  .canvas { position: relative; width: 1200px; height: 1000px; }
  .brochure {
    position: absolute; left: 25px; top: 48px; width: 1145px; height: 887px;
    box-shadow: 0 4px 14px rgba(0,0,0,.25);
    display: flex;
  }
  .panel { position: relative; height: 100%; }
  .panel--pricing { width: 381px; background: var(--page); }
  .panel--contact { width: 383px; background: var(--panel-mid); }
  .panel--cover { width: 381px; background: var(--slate); overflow: hidden; }

  /* pricing panel */
  .photo-copier {
    position: absolute; left: 0; top: 0; width: 381px; height: 322px;
    background: radial-gradient(ellipse at 55% 65%, #c9cbcd 0%, #8f9296 30%, #2a2a2c 62%, #0b0b0c 100%);
  }
  .pricing-title {
    position: absolute; left: 24px; top: 343px;
    font: 300 35px/1 'Oswald', sans-serif; color: var(--heading-blue);
  }
  .pricing-rule { position: absolute; left: 0; top: 392px; width: 291px; height: 3px; background: var(--slate-dark); }
  .pricing-copy {
    position: absolute; left: 25px; top: 420px; width: 335px;
    font: 400 16.5px/1.3 'Source Sans 3', sans-serif; color: var(--ink);
  }
  .pricing-copy p + p { margin-top: 21px; }

  /* contact panel */
  .contact {
    position: absolute; left: 0; top: 588px; width: 100%; text-align: center;
    font: 400 18.5px/24.5px 'Source Sans 3', sans-serif; color: var(--ink);
  }
  .contact-title {
    font: 400 26px/1 'Oswald', sans-serif; color: var(--contact-navy); margin-bottom: 13px;
  }

  /* cover panel */
  .cover-top { position: absolute; left: 0; top: 0; width: 100%; height: 472px; background: var(--navy-dark); }
  .brand {
    position: absolute; right: 22px; top: 32px;
    font: 400 29px/1 'Oswald', sans-serif; color: var(--white);
  }
  .brand-rule { position: absolute; left: 0; top: 74px; width: 100%; height: 1px; background: #7f8a94; }
  .guide-v { position: absolute; left: 41px; top: 0; height: 436px; border-left: 1px dashed #7f8a94; }
  .guide-h { position: absolute; left: 0; top: 436px; width: 100%; border-top: 1px dashed #7f8a94; }
  .photo-commuters {
    position: absolute; left: 0; top: 189px; width: 100%; height: 141px;
    background: linear-gradient(90deg, #f2f3f4 0%, #d9dcdf 45%, #8d949b 75%, #c4c8cc 100%);
  }
  .headline {
    position: absolute; left: 15px; top: 214px;
    font: 300 25px/33px 'Oswald', sans-serif; color: #1a1f26;
  }
  .headline strong { font-weight: 500; color: var(--accent-red); }
  .locations-bar {
    position: absolute; left: 0; top: 472px; width: 100%; height: 34px;
    background: var(--bar-light); white-space: nowrap;
    font: 400 15px/34px 'Oswald', sans-serif; color: #2a2f35; padding-left: 7px; letter-spacing: -.3px;
  }
  .courts { position: absolute; left: 28px; top: 530px; list-style: none; }
  .courts li {
    position: relative; padding-left: 32px;
    font: 400 15px/19px 'Source Sans 3', sans-serif; color: var(--white);
  }
  .courts li svg { position: absolute; left: 0; top: 1px; }
  .courts li:nth-child(1) { margin-bottom: 17px; }
  .courts li:nth-child(2) { margin-bottom: 21px; }
  .courts li:nth-child(3) { margin-bottom: 18px; }
  .ask {
    position: absolute; left: 40px; top: 728px; width: 190px; text-align: center;
    font: 300 19px/27px 'Oswald', sans-serif; color: var(--white);
  }
  .badge { position: absolute; left: 234px; top: 689px; width: 120px; height: 120px; }

  /* footer */
  .footer-line { position: absolute; top: 838px; height: 4px; }
  .footer-line--left { left: 0; width: 381px; background: var(--pill-grey); }
  .footer-line--mid { left: 381px; width: 383px; background: var(--slate-dark); }
  .footer-line--right { left: 764px; width: 381px; background: var(--pill-light); }
  .pill {
    position: absolute; top: 829px; height: 25px; border-radius: 13px; text-align: center;
    font: 400 14px/25px 'Source Sans 3', sans-serif; letter-spacing: 1.6px; white-space: nowrap;
  }
  .pill--email { left: 35px; width: 298px; background: var(--pill-grey); color: #2c2c2c; }
  .pill--tagline { left: 422px; width: 299px; background: var(--slate-dark); color: var(--white); font: 400 14px/25px 'Oswald', sans-serif; letter-spacing: .4px; }
  .pill--web { left: 811px; width: 300px; background: var(--pill-light); color: #2c2c2c; }
</style>
</head>
<body>
<div class="canvas">
  <div class="brochure">
    <section class="panel panel--pricing">
      <div class="photo-copier" role="img" aria-label="Photo of a hand placing a sheet on a photocopier glass"></div>
      <h2 class="pricing-title">Photocopying Pricing</h2>
      <div class="pricing-rule"></div>
      <div class="pricing-copy">
        <p>With our new systems and process we have developed a unique way of reducing our costs and can save you more than 35% over our competitors.</p>
        <p>Contact us for a quote today!&nbsp; Simply provide your instructions via email to us directly.</p>
      </div>
    </section>

    <section class="panel panel--contact">
      <div class="contact">
        <h2 class="contact-title">Contact Us</h2>
        <p>Email: info@brindlefax-demo.com.au</p>
        <p>Fax: 02 5550 0142</p>
        <p>Telephone: 95550173</p>
        <p>DX 40417 Sydney Downtown</p>
        <p>118/42 Larkspur Street, Sydney</p>
        <p>NSW 2001</p>
        <p>www.brindlefax-demo.com.au</p>
      </div>
    </section>

    <section class="panel panel--cover">
      <div class="cover-top"></div>
      <div class="guide-v"></div>
      <div class="guide-h"></div>
      <div class="brand">Brindlefax Services Pty Ltd.</div>
      <div class="brand-rule"></div>
      <div class="photo-commuters" role="img" aria-label="Motion-blurred photo of business people walking through a city lobby"></div>
      <h1 class="headline">Need Important<br>Legal Documents<br>Delivered <strong>Urgently?</strong></h1>
      <div class="locations-bar">Onsite copying and Uplifting of documents and Court records at:</div>
      <ul class="courts">
        <li><svg width="20" height="20" viewBox="0 0 20 20"><circle cx="10" cy="10" r="8.5" fill="none" stroke="var(--icon-blue)" stroke-width="1.5"/><polygon points="10,4.5 15.2,8.3 13.2,14.5 6.8,14.5 4.8,8.3" fill="none" stroke="var(--icon-blue)" stroke-width="1.5"/></svg>Local Courts – Harbourline Centre Sydney and<br>Elm Parade Tower</li>
        <li><svg width="20" height="20" viewBox="0 0 20 20"><circle cx="10" cy="10" r="8.5" fill="none" stroke="var(--icon-blue)" stroke-width="1.5"/><polygon points="10,4.5 15.2,8.3 13.2,14.5 6.8,14.5 4.8,8.3" fill="none" stroke="var(--icon-blue)" stroke-width="1.5"/></svg>District Courts</li>
        <li><svg width="20" height="20" viewBox="0 0 20 20"><circle cx="10" cy="10" r="8.5" fill="none" stroke="var(--icon-blue)" stroke-width="1.5"/><polygon points="10,4.5 15.2,8.3 13.2,14.5 6.8,14.5 4.8,8.3" fill="none" stroke="var(--icon-blue)" stroke-width="1.5"/></svg>NSW Supreme Court</li>
        <li><svg width="20" height="20" viewBox="0 0 20 20"><circle cx="10" cy="10" r="8.5" fill="none" stroke="var(--icon-blue)" stroke-width="1.5"/><polygon points="10,4.5 15.2,8.3 13.2,14.5 6.8,14.5 4.8,8.3" fill="none" stroke="var(--icon-blue)" stroke-width="1.5"/></svg>Family Court</li>
      </ul>
      <p class="ask">Ask our Frienly Staff<br>For Our Pricing</p>
      <svg class="badge" viewBox="0 0 120 120">
        <defs>
          <radialGradient id="burst-fill" cx="50%" cy="50%" r="50%">
            <stop offset="0%" stop-color="#bfe6fb"/>
            <stop offset="100%" stop-color="#4fb3e6"/>
          </radialGradient>
        </defs>
        <polygon fill="url(#burst-fill)" points="116,60 107.4,67.5 113.3,77.3 102.8,81.8 105.3,92.9 93.9,93.9 92.9,105.3 81.8,102.8 77.3,113.3 67.5,107.4 60,116 52.5,107.4 42.7,113.3 38.2,102.8 27.1,105.3 26.1,93.9 14.7,92.9 17.2,81.8 6.7,77.3 12.6,67.5 4,60 12.6,52.5 6.7,42.7 17.2,38.2 14.7,27.1 26.1,26.1 27.1,14.7 38.2,17.2 42.7,6.7 52.5,12.6 60,4 67.5,12.6 77.3,6.7 81.8,17.2 92.9,14.7 93.9,26.1 105.3,27.1 102.8,38.2 113.3,42.7 107.4,52.5"/>
        <circle cx="60" cy="60" r="41" fill="#e8f6fe"/>
        <circle cx="60" cy="60" r="37" fill="#1b4f8c"/>
        <text x="60" y="56" text-anchor="middle" font-family="Oswald, sans-serif" font-weight="500" font-size="20" fill="#ffffff">SAVE</text>
        <text x="60" y="80" text-anchor="middle" font-family="Oswald, sans-serif" font-weight="500" font-size="20" fill="#ffffff">30%</text>
      </svg>
    </section>

    <div class="footer-line footer-line--left"></div>
    <div class="footer-line footer-line--mid"></div>
    <div class="footer-line footer-line--right"></div>
    <div class="pill pill--email">info@brindlefax-demo.com.au</div>
    <div class="pill pill--tagline">SAVE TIME AND UP TO 35% OF COSTS</div>
    <div class="pill pill--web">www.brindlefax-demo.com.au</div>
  </div>
</div>
</body>
</html>
```